Consulting Firm stationery design

Now that the ArtHive has given us a new logo we'll now need to have all our stationery designed. So we're asking for this community to help us once again.We're looking to get from you Letterheads (Header and Footer, suitable to be applied on a .docx format. Vectors are required but keep this in mind), Envelopes (Front and Back designs, back is not a must but desirable depending on your design), 9"x 12" Pocket Folders (consider design for front and back, also for pockets as well), Business Cards.An elegant design is a must have, mostly for Folders and Envelopes. The idea with this two is to stand out from others when they're handed over. Ideas are welcomed, we were thinking maybe on some texturing simulation for these.Folders will have 3 addresses and contact information. Envelopes will have 1 address and contact information.Brand Manual attached. marquesino logo has been copyrighted already. I'm also attaching the current stationary designs (these never got to be out for production but was going to be before we made the brand changes); Pocker folders page 1 to 4 (pages 2 and 4 are the pocket designs), Pages 5 and 6 (6 is the back of the envelope), Pages 7 and 8 (8 is the back of the business card). No letterhead within these designs as it just had the logo and address.

Industry/Entity Type

Business Consultant

Font styles to use
Serif
Sans Serif

Requirements
Must have
• Elegance
Nice to have
• Modern looking out of common

```html
<!DOCTYPE html>
<html lang="en">
<head>
<meta charset="utf-8">
<title>marquesino business card</title>
<link rel="stylesheet" href="https://fonts.googleapis.com/css2?family=Poppins:wght@400;500;600&display=swap">
<style>
  :root {
    --brand-blue: #1873a4;
    --ink: #2b2b2b;
    --ink-soft: #444444;
    --band-grey: #383838;
    --paper: #ffffff;
    --backdrop: #e9e9e9;
    --divider: #9a9a9a;
  }
  * { margin: 0; padding: 0; box-sizing: border-box; }
  html, body {
    width: 1200px; height: 960px; overflow: hidden;
    background: var(--backdrop);
    font-family: "Poppins", sans-serif;
  }
  .canvas { position: relative; width: 1200px; height: 960px; }

  .card { position: absolute; left: 261px; width: 679px; height: 388px; }

  /* Front */
  .card-front { top: 61px; background: var(--paper); box-shadow: 0 2px 6px rgba(0,0,0,.18); }
  .card-front .edge-bar { position: absolute; left: 0; top: 0; width: 15px; height: 100%; background: var(--brand-blue); }
  .brand-block { position: absolute; left: 40px; top: 150px; width: 300px; text-align: center; }
  .wordmark { display: inline-flex; align-items: center; gap: 10px; font-weight: 600; font-size: 40px; letter-spacing: -0.5px; line-height: 1; }
  .wordmark .dot { width: 14px; height: 14px; border-radius: 50%; background: var(--brand-blue); }
  .card-front .wordmark { color: var(--ink); }
  .tagline { margin-top: 66px; color: var(--brand-blue); font-size: 14.5px; font-weight: 500; letter-spacing: .2px; }

  .divider { position: absolute; left: 321px; top: 52px; width: 1px; height: 288px; background: linear-gradient(var(--paper), var(--divider) 20%, var(--divider) 80%, var(--paper)); }

  .contact { position: absolute; left: 347px; top: 46px; color: var(--ink-soft); font-size: 14px; line-height: 17px; }
  .person-name { font-size: 19px; font-weight: 600; color: var(--ink); line-height: 24px; }
  .person-name .role { font-weight: 400; font-size: 16px; }
  .credentials { font-size: 11.5px; line-height: 14px; margin-bottom: 6px; }
  .group { margin-bottom: 11px; }
  .firm-name { font-weight: 500; font-size: 13.5px; color: var(--ink); }
  .web { color: var(--brand-blue); }

  /* Back */
  .card-back { top: 511px; background: var(--brand-blue); box-shadow: 0 2px 6px rgba(0,0,0,.18); }
  .card-back .brand-block { left: 0; width: 679px; top: 150px; }
  .card-back .wordmark { color: var(--paper); font-size: 56px; }
  .card-back .wordmark .dot { width: 18px; height: 18px; background: var(--paper); }
  .partner-band { position: absolute; left: 0; top: 319px; width: 100%; height: 36px; background: var(--band-grey); }
  .partner-badge { position: absolute; top: 9px; height: 18px; border-radius: 9px; background: #ffffff; opacity: .9; }
  .badge-one { left: 37px; width: 84px; }
  .badge-two { left: 280px; width: 121px; border-radius: 3px; }
  .badge-three { left: 550px; width: 80px; border-radius: 3px; }
</style>
</head>
<body>
<main class="canvas">
  <section class="card card-front">
    <div class="edge-bar"></div>
    <div class="brand-block">
      <div class="wordmark"><span>marquesino</span><span class="dot"></span></div>
      <p class="tagline">Consultancy • Audit • Analytics</p>
    </div>
    <div class="divider"></div>
    <div class="contact">
      <p class="person-name">Elian R. Mota <span class="role">| COO &amp; Partner</span></p>
      <p class="credentials">ITC,MSMIT, Vexa Certified, CISA<br>PredictiveAnalytics</p>
      <div class="group">
        <p>(809) 555 0142 ext. 201</p>
        <p>(809) 555 0187</p>
        <p>elian@marquesino.do</p>
      </div>
      <div class="group">
        <p class="firm-name">MARQUESINO SRL</p>
        <p>Alameda Business Center</p>
        <p>Calle Los Almendros 42, Bella Vista</p>
        <p>Santo Domingo, Rep. Dominicana</p>
      </div>
      <div class="group">
        <p>(809) 555 0142</p>
        <p>info@marquesino.do</p>
        <p class="web">www.marquesino.do</p>
      </div>
      <p>MARQUESINO SRL</p>
      <p>DR member firm of marquesino LLC</p>
    </div>
  </section>

  <section class="card card-back">
    <div class="brand-block">
      <div class="wordmark"><span>marquesino</span><span class="dot"></span></div>
    </div>
    <div class="partner-band">
      <span class="partner-badge badge-one"></span>
      <span class="partner-badge badge-two"></span>
      <span class="partner-badge badge-three"></span>
    </div>
  </section>
</main>
</body>
</html>
```